Wine Shop Banners

Banner graphic/images required
Require banner images to match the present online wine shop.

www.korbel-traube-laden.de

The wine-shop presently has a very clean, simple design, lots of white space, which is very much the trend at the moment.

Requirements
Images or graphic design for present banners visible on the homepage

The colour and feeling of the banners must fit in with the present clean, simple design.

Work required
3 large slide-card/banners (can be more) and 3 smaller fixed banners below. Please view website to see present position of banners.

LARGE BANNERS x 3

Something special with white background within the banner space
White background on each slide-card. Small individual graphic image in the middle of the slide card. This could be either a simple element of wine:
ingredients, fruit (grape), bottle, cork, old bottle label etc. just displaying one item on each slide-card. Preferably with high quality graphic features.

Note:
We are trying the steer away from the classic stereotype wineshop design. The image/s should have a higher, individual graphic touch, which gives the design something different. Sometimes such artistic work is displayed in steampunk or even in nostalgic design, which leaves the viewer slightly memorized with the content.
To clarify: we are not looking for a full steampunk design but possibly certain elements of this will give you an idea what we mean. That is to say, the design can go slightly in this direction without going over the top. Something small but very eye-catching.

SMALLER BANNERS x 3

One idea is:
Showing a symbol e.g. - discount sign "%" against a white background but again with a high graphic quality.

Target Market(s)

People interested in purchasing wine.
Ages approx. 25 to 65

Industry/Entity Type

Shop

Requirements
Must have
• Something special with white background
• Small individual graphic image in the middle of the slide card.
Nice to have
• The image/s should have a higher, individual graphic touch, which gives the design something different. Something that leaves the viewer slightly memorized with the content.
Should not have
• Not the typical classical design that is often seen on wine shops.

```html
<!DOCTYPE html>
<html lang="de">
<head>
<meta charset="utf-8">
<title>Verdalu Wein Shop</title>
<link href="https://fonts.googleapis.com/css2?family=Cinzel:wght@400;500&family=Libre+Baskerville:wght@400;700&family=Open+Sans:wght@400;600&display=swap" rel="stylesheet">
<style>
:root{
  --wine:#a3264a;
  --olive:#5b5a3c;
  --lime:#cfdc5c;
  --lime-text:#a9b83a;
  --text:#555;
  --muted:#8a8a8a;
  --line:#e4e4e4;
  --bg:#ffffff;
}
*{box-sizing:border-box;margin:0;padding:0}
html,body{width:1200px;height:840px;overflow:hidden;background:var(--bg)}
body{font-family:"Open Sans",sans-serif;color:var(--text);position:relative}
.page{position:absolute;left:150px;top:0;width:900px;height:840px}

.header{position:absolute;left:0;top:28px;width:900px;height:70px}
.brand{position:absolute;left:0;top:6px;font-family:"Cinzel",serif;font-weight:500;font-size:26px;letter-spacing:3px;color:var(--olive);line-height:1}
.brand-sub{display:block;font-size:11px;letter-spacing:6px;margin-top:6px}
.search{position:absolute;left:470px;top:10px;display:flex;height:26px}
.search-field{width:230px;border:1px solid #bbb;display:flex;align-items:center;gap:8px;padding-left:8px;font-size:11px;color:#999}
.search-go{width:36px;background:var(--wine);color:#fff;font-size:11px;font-weight:600;display:flex;align-items:center;justify-content:center}
.login{position:absolute;right:0;top:12px;font-size:13px;color:var(--muted)}

.nav{position:absolute;left:0;top:106px;width:900px;display:flex;gap:30px;font-size:14px;color:#444}
.nav .soft{color:var(--muted)}
.nav-tools{position:absolute;right:0;top:-2px;display:flex;gap:16px;font-size:12px;color:var(--muted);align-items:center}
.nav-tools span{display:flex;align-items:center;gap:5px}

.sidebar{position:absolute;left:0;top:148px;width:200px}
.filter-bar{background:var(--lime);color:#3d3d2a;font-size:12px;font-weight:600;padding:8px 10px;letter-spacing:.3px}
.filter-title{color:var(--lime-text);font-size:11px;font-weight:600;margin:14px 0 6px;letter-spacing:.5px}
.filter-list{list-style:none;font-size:12px;line-height:20px;color:#444}
.filter-list li::before{content:"›";margin-right:6px;color:#666}
.filter-list em{font-style:normal;color:var(--muted)}
.scroll-box{position:relative;height:122px;overflow:hidden;padding-right:16px}
.scroll-track{position:absolute;right:0;top:0;width:6px;height:122px;background:#eee}
.scroll-thumb{position:absolute;right:0;top:8px;width:6px;height:52px;background:#bbb}
.price-slider{position:relative;height:22px;margin-top:4px}
.price-track{position:absolute;left:4px;right:4px;top:8px;height:4px;background:#e6e6e6;border:1px solid #ccc}
.price-knob{position:absolute;top:3px;width:12px;height:12px;border:1px solid #aaa;border-radius:50%;background:#fff}
.price-label{text-align:center;font-size:11px;color:#666}
.region-box{border:1px solid var(--line);height:26px;margin-top:4px}

.main{position:absolute;left:220px;top:148px;width:680px}
.hero{position:relative;height:300px;background:#fafafa;border:1px solid var(--line);overflow:hidden}
.hero-art{position:absolute;right:0;top:0;width:360px;height:300px;background:radial-gradient(circle at 65% 40%,#3a3a3a 0 14%,transparent 15%),radial-gradient(circle at 40% 70%,#9e2234 0 12%,transparent 13%),linear-gradient(120deg,#f4f4f4,#e2e2e2)}
.hero-text{position:absolute;left:44px;top:82px}
.kicker{font-family:"Cinzel",serif;color:var(--wine);font-size:12px;letter-spacing:.5px}
.hero-title{font-family:"Cinzel",serif;font-weight:400;color:var(--olive);font-size:44px;line-height:46px;margin-top:8px}
.hero-sub{font-family:"Libre Baskerville",serif;font-size:11px;color:var(--olive);margin-top:14px}

.promos{display:flex;gap:8px;margin-top:10px}
.promo{position:relative;flex:1;height:112px;border:1px solid var(--line);text-align:center;overflow:hidden;background:linear-gradient(#f3f3f0,#fff 45%)}
.promo-content{position:relative;padding-top:26px}
.promo-title{font-family:"Cinzel",serif;color:var(--olive);font-size:24px;line-height:26px}
.promo-note{font-family:"Libre Baskerville",serif;font-size:8px;color:var(--olive);letter-spacing:.5px;margin-top:4px}
.promo-figure{font-family:"Libre Baskerville",serif;color:var(--wine);font-size:22px;line-height:26px;margin-top:2px}
.promo-figure.big{font-size:34px;line-height:34px}
.promo-figure small{font-size:14px}

.products-head{display:flex;align-items:center;justify-content:space-between;margin-top:22px}
.products-title{font-family:"Libre Baskerville",serif;font-weight:700;font-size:15px;color:#333;display:flex;align-items:center;gap:8px}
.pager{display:flex;gap:3px}
.pager span{width:18px;height:18px;border:1px solid #aaa;display:flex;align-items:center;justify-content:center}
.product-row{display:flex;gap:4px;margin-top:10px}
.product{flex:1;height:220px;border:1px solid var(--line);text-align:center}
.bottle{height:160px;margin:14px auto 8px;width:60px}
.product-name{font-size:11px;color:#666}
</style>
</head>
<body>
<div class="page">
  <header class="header">
    <div class="brand">VERDALU<span class="brand-sub">WEIN SHOP</span></div>
    <div class="search">
      <div class="search-field">
        <svg width="11" height="11" viewBox="0 0 12 12"><circle cx="5" cy="5" r="3.6" fill="none" stroke="#a3264a" stroke-width="1.6"/><line x1="7.6" y1="7.6" x2="11" y2="11" stroke="#a3264a" stroke-width="1.6"/></svg>
        Suche
      </div>
      <div class="search-go">GO</div>
    </div>
    <div class="login">Anmelden</div>
  </header>

  <nav class="nav">
    <span>Rotwein</span><span>Weißwein</span><span>Rosewein</span><span>Sekt / Champagner</span>
    <span class="soft">Sonderangebote</span><span class="soft">Probierpakete</span>
    <div class="nav-tools">
      <span><svg width="18" height="15" viewBox="0 0 18 15"><path d="M1 1h3l2 9h9l2-6H5" fill="none" stroke="#666" stroke-width="1.2"/><circle cx="7" cy="13" r="1.2" fill="#666"/><circle cx="14" cy="13" r="1.2" fill="#666"/></svg>(0)</span>
      <span><svg width="16" height="14" viewBox="0 0 16 14"><path d="M8 13 1.8 6.8A3.4 3.4 0 0 1 8 2.6a3.4 3.4 0 0 1 6.2 4.2Z" fill="none" stroke="#666" stroke-width="1.2"/></svg>(0)</span>
    </div>
  </nav>

  <aside class="sidebar">
    <div class="filter-bar">DETAILSUCHE</div>
    <div class="filter-title">LAND</div>
    <div class="scroll-box">
      <ul class="filter-list">
        <li>Italien <em>(90)</em></li><li>Frankreich <em>(74)</em></li><li>Deutschland <em>(60)</em></li>
        <li>Spanien <em>(35)</em></li><li>Südafrika <em>(15)</em></li><li>Australien <em>(12)</em></li>
        <li>Österreich <em>(11)</em></li>
      </ul>
      <div class="scroll-track"><div class="scroll-thumb"></div></div>
    </div>
    <div class="filter-title">GESCHMACK</div>
    <ul class="filter-list">
      <li>Trocken <em>(305)</em></li><li>Halbtrocken <em>(10)</em></li><li>Lieblich <em>(6)</em></li>
      <li>Süß <em>(2)</em></li><li>Edelsüss <em>(1)</em></li>
    </ul>
    <div class="filter-title">FARBE</div>
    <ul class="filter-list">
      <li>Rot <em>(157)</em></li><li>Weiß <em>(128)</em></li><li>Prickelnd <em>(23)</em></li>
      <li>Rosé <em>(13)</em></li><li>Champagner <em>(9)</em></li>
    </ul>
    <div class="filter-title">PREIS</div>
    <div class="price-slider"><div class="price-track"></div><div class="price-knob" style="left:0"></div><div class="price-knob" style="right:0"></div></div>
    <div class="price-label">2 € - 75 €</div>
    <div class="filter-title">REGION</div>
    <div class="region-box"></div>
  </aside>

  <main class="main">
    <section class="hero">
      <div class="hero-art" role="img" aria-label="Illustration: Rotweinflasche in Seidenpapier mit roten Trauben"></div>
      <div class="hero-text">
        <div class="kicker">LOREM IPSUM DOLOR SIT AMET, CONSECTETUR</div>
        <h1 class="hero-title">ROYAL QUALITY<br>WINE</h1>
        <div class="hero-sub">Surprise of Wine Gifts for Someone Special</div>
      </div>
    </section>

    <section class="promos">
      <div class="promo" role="img" aria-label="Banner mit blasser Weinberg-Gravur: Free Shipping">
        <div class="promo-content">
          <div class="promo-title">FREE SHIPPING</div>
          <div class="promo-note">ON ORDERS OVER</div>
          <div class="promo-figure">$25</div>
        </div>
      </div>
      <div class="promo" role="img" aria-label="Banner mit blasser Weinberg-Gravur: Celebrate">
        <div class="promo-content" style="padding-top:34px">
          <div class="promo-title">CELEBRATE</div>
          <div class="promo-note">YOUR ANNIVERSARY WITH TASTE</div>
        </div>
      </div>
      <div class="promo" role="img" aria-label="Banner mit blasser Weinberg-Gravur: Special Offer">
        <div class="promo-content">
          <div class="promo-title">SPECIAL OFFER</div>
          <div class="promo-figure big"><small>OFF</small> 20%</div>
        </div>
      </div>
    </section>

    <div class="products-head">
      <div class="products-title">
        <svg width="12" height="12" viewBox="0 0 12 12"><circle cx="6" cy="6" r="5" fill="none" stroke="#a3264a" stroke-width="1.2"/><path d="M5 3.5 7.5 6 5 8.5" fill="none" stroke="#a3264a" stroke-width="1.2"/></svg>
        Ausgewählte Produkte
      </div>
      <div class="pager">
        <span><svg width="8" height="8" viewBox="0 0 8 8"><path d="M5.5 1 2.5 4l3 3" fill="none" stroke="#666"/></svg></span>
        <span><svg width="8" height="8" viewBox="0 0 8 8"><path d="M2.5 1l3 3-3 3" fill="none" stroke="#666"/></svg></span>
      </div>
    </div>
    <div class="product-row">
      <div class="product"><div class="bottle" role="img" aria-label="Flasche Roséschaumwein" style="background:linear-gradient(90deg,#e9a9a9,#f4cccc,#d98c8c)"></div><div class="product-name">Rosé Brut, Casa Lentari</div></div>
      <div class="product"><div class="bottle" role="img" aria-label="Flasche Weißwein" style="background:linear-gradient(90deg,#6f6a3a,#b9b27a,#5c5830)"></div><div class="product-name">Bianco Valle Orsina</div></div>
      <div class="product"><div class="bottle" role="img" aria-label="Flasche Rotwein" style="background:linear-gradient(90deg,#111,#3a3a3a,#111)"></div><div class="product-name">Coteaux, Domaine Belvaux</div></div>
      <div class="product"><div class="bottle" role="img" aria-label="Flasche Dessertwein" style="background:linear-gradient(90deg,#8a5a1e,#d6b07a,#7a4c18)"></div><div class="product-name">Vino Dolce Riserva Ferla</div></div>
    </div>
  </main>
</div>
</body>
</html>
```